BrightLedger, The Ultimate Franchise Online Training Platform

Need Roll-up Banner Design measuring 30 x 80 inches, Looking for a design that is clean, professional, not cliche. We’re open to shape motifs like a circle, square, or swoosh—choose what best reinforces motion, strength, or innovation. Consistency is key: this should look great whether it's on a banner, a slide deck, or our letterhead. Our business is serving as a Franchisee e-learning platform providing vetted information from experts, an online library and masterclasses. Uploaded examples of Banner art with correct wording. Wording can be:
THE ULTIMATE FRANCHISEE TOOLKIT
Your 24/7 Edge for Franchise Success
On-Demand Resource Library
Monthly Masterclasses
Direct Access to Industry Experts
“Your Entrepreneurial Edge.”
OR
“Opening your first or your fifth, BrightLedger is your unfair advantage.”
Catapult your learning curve.
Avoid costly mistakes.
Grow with a community that gets it.
Join the Movement. Unlock Your Toolkit Today.
Updates

My apologies to designers I haven´t voted or provided updates for yet. We are still reviewing designs as the last call will be made by the owners and we live in different time zones. Thank you!

Target Market(s)

Business Owners, from small to mid

Industry/Entity Type

Small Business Owners, Franchisees

Font styles to use
Other font styles liked:
• Poppins, Roboto, Garamond, Montserrat, Lato

Colors

Designer to choose colors to be used in the design.

Requirements
Must have
• Consistency in color guide, font and wording
Nice to have
• Open to pretty much fluid designs, simple and uncluttered

```html
<!DOCTYPE html>
<html lang="en">
<head>
<meta charset="utf-8">
<title>BrightLedger Roll-up Banner</title>
<link href="https://fonts.googleapis.com/css2?family=Montserrat:wght@300;400;800;900&display=swap" rel="stylesheet">
<style>
  :root {
    --ink: #000000;
    --forest: #262c1f;
    --lime: #a6cd3f;
    --paper: #ffffff;
    --stage: #e6e6e6;
  }
  html, body {
    margin: 0;
    padding: 0;
    width: 1200px;
    height: 1200px;
    overflow: hidden;
    background: var(--stage);
  }
  .banner {
    position: absolute;
    left: 390px;
    top: 40px;
    width: 420px;
    height: 1120px;
    display: block;
    font-family: 'Montserrat', sans-serif;
  }
  .headline { font-weight: 900; fill: var(--ink); }
  .lead-lime { fill: var(--lime); }
  .lead-ink { fill: var(--ink); }
  .light { font-weight: 400; }
  .heavy { font-weight: 800; }
  .brand-name { font-weight: 300; fill: var(--lime); }
  .claim { font-weight: 400; fill: var(--paper); }
  .benefit { font-weight: 400; fill: var(--lime); }
  .cta { font-weight: 800; fill: var(--forest); }
  .web { font-weight: 800; fill: var(--paper); }
  .web-name { fill: var(--lime); }
</style>
</head>
<body>
<svg class="banner" viewBox="0 0 472 1260" xmlns="http://www.w3.org/2000/svg" role="img" aria-label="BrightLedger roll-up banner">
  <rect class="panel-top" x="0" y="0" width="472" height="320" fill="var(--paper)"/>
  <rect class="panel-bottom" x="0" y="320" width="472" height="940" fill="var(--forest)"/>

  <text class="headline" x="236" y="145" font-size="72" text-anchor="middle" textLength="362" lengthAdjust="spacingAndGlyphs">OPENING</text>
  <text x="237" y="202" font-size="46" text-anchor="middle" textLength="306" lengthAdjust="spacingAndGlyphs" class="lead-lime"><tspan class="light">YOUR </tspan><tspan class="heavy">FIRST</tspan></text>
  <text x="243" y="258" font-size="46" text-anchor="middle" textLength="382" lengthAdjust="spacingAndGlyphs" class="lead-ink"><tspan class="light" font-size="32">OR </tspan><tspan class="light">YOUR </tspan><tspan class="heavy">FIFTH,</tspan></text>

  <rect class="brand-square" x="52" y="414" width="62" height="62" fill="var(--lime)"/>
  <text class="brand-name" x="136" y="476" font-size="72" textLength="286" lengthAdjust="spacingAndGlyphs">BRIGHT</text>
  <text class="brand-name" x="136" y="572" font-size="72" textLength="286" lengthAdjust="spacingAndGlyphs">LEDGER</text>

  <text class="claim" x="236" y="735" font-size="50" text-anchor="middle" textLength="398" lengthAdjust="spacingAndGlyphs">IS YOUR UNFAIR</text>
  <text class="claim" x="229" y="790" font-size="50" text-anchor="middle" textLength="320" lengthAdjust="spacingAndGlyphs">ADVANTAGE.</text>

  <text class="benefit" x="238" y="843" font-size="20" text-anchor="middle" textLength="356" lengthAdjust="spacingAndGlyphs">CATAPULT YOUR LEARNING CURVE.</text>
  <line class="benefit-rule" x1="62" y1="856" x2="382" y2="856" stroke="var(--lime)" stroke-width="2"/>
  <text class="benefit" x="238" y="890" font-size="20" text-anchor="middle" textLength="258" lengthAdjust="spacingAndGlyphs">AVOID COSTLY MISTAKES.</text>
  <line class="benefit-rule" x1="62" y1="903" x2="382" y2="903" stroke="var(--lime)" stroke-width="2"/>
  <text class="benefit" x="238" y="937" font-size="20" text-anchor="middle" textLength="418" lengthAdjust="spacingAndGlyphs">GROW WITH A COMMUNITY THAT GETS IT.</text>

  <rect class="cta-band" x="0" y="970" width="472" height="155" fill="var(--lime)"/>
  <polygon class="cta-tail" points="302,1124 402,1124 282,1165" fill="var(--lime)"/>
  <text class="cta" x="238" y="1015" font-size="34" text-anchor="middle" textLength="392" lengthAdjust="spacingAndGlyphs">JOIN THE MOVEMENT</text>
  <text class="cta" x="243" y="1058" font-size="34" text-anchor="middle" textLength="262" lengthAdjust="spacingAndGlyphs">UNLOCK YOUR</text>
  <text class="cta" x="243" y="1102" font-size="34" text-anchor="middle" textLength="288" lengthAdjust="spacingAndGlyphs">TOOLKIT TODAY</text>

  <text class="web" x="246" y="1210" font-size="32" text-anchor="middle" textLength="406" lengthAdjust="spacingAndGlyphs">www.<tspan class="web-name">BRIGHTLEDGER</tspan>.com</text>
</svg>
</body>
</html>
```